VFX Company Business Card Design Project

The Ember Vale is a decentralized Visual Effects Studio servicing the television and feature film industries.
Project Brief:
Take our logo that was previously designed on Pixel Harbor and make a double sided business card.
Requirements:
- Card MUST be double sided.
- Front of card MUST have the yellow part of our logo against the dark grey background.
- Back of card is completely up to the designer.
- Back of card must include the complete company logo.
Please follow these File Preparation guidelines:
http://printmoor.example/infopage?file=filetype_en&s=PrintMoor_new&lang=en
Industry/Entity Type
Business
Look and feel
Each slider illustrates characteristics of the customer's brand and the style your logo design should communicate.

```html
<!DOCTYPE html>
<html lang="en">
<head>
<meta charset="utf-8">
<title>The Ember Vale – Business Card</title>
<link rel="stylesheet" href="https://fonts.googleapis.com/css2?family=Jost:wght@400;500;600&display=swap">
<style>
  :root {
    --backdrop: #d4d5d7;
    --card-dark: #262626;
    --brand-yellow: #fbc82b;
    --logo-grey: #c9cdd0;
    --ink-dark: #2a2a2a;
    --white: #ffffff;
    --debris-light: #6f6f68;
    --debris-dark: #2e2e2c;
  }
  * { box-sizing: border-box; margin: 0; padding: 0; }
  html, body {
    width: 1200px;
    height: 902px;
    overflow: hidden;
    background: var(--backdrop);
    font-family: "Jost", "Futura", sans-serif;
  }
  .card {
    position: absolute;
    left: 320px;
    width: 563px;
    height: 364px;
    background: var(--card-dark);
    overflow: hidden;
  }
  .card--front { top: 58px; }
  .card--back { top: 506px; }

  .brand {
    position: absolute;
    left: 36px;
    display: flex;
    align-items: center;
    gap: 12px;
  }
  .card--front .brand { top: 44px; }
  .card--back .brand { top: 40px; }
  .brand__dot {
    width: 36px;
    height: 36px;
    border-radius: 50%;
    background: var(--brand-yellow);
  }
  .brand__name {
    font-weight: 500;
    font-size: 30px;
    line-height: 1;
    color: var(--logo-grey);
    letter-spacing: 0.5px;
  }

  .info-panel {
    position: absolute;
    left: 185px;
    top: 119px;
    width: 378px;
    height: 212px;
    background: var(--brand-yellow);
  }
  .info-panel__tagline {
    position: absolute;
    left: 58px;
    top: 72px;
    font-weight: 500;
    font-size: 23px;
    color: var(--white);
  }
  .info-panel__rule {
    position: absolute;
    left: 48px;
    top: 156px;
    width: 3px;
    height: 56px;
    background: var(--white);
  }
  .contact {
    position: absolute;
    left: 58px;
    top: 157px;
    list-style: none;
    font-size: 17px;
    line-height: 22px;
    color: var(--ink-dark);
  }
  .contact__label { font-weight: 600; }

  .debris-art {
    position: absolute;
    left: 17px;
    top: 90px;
    width: 528px;
    height: 213px;
    background: radial-gradient(ellipse at 50% 70%, var(--debris-light) 0%, var(--debris-dark) 55%, var(--card-dark) 80%);
  }
  .web {
    position: absolute;
    right: 37px;
    top: 314px;
    font-weight: 600;
    font-size: 20px;
    color: var(--brand-yellow);
  }
</style>
</head>
<body>
  <section class="card card--front">
    <div class="brand">
      <span class="brand__dot"></span>
      <span class="brand__name">The Ember Vale</span>
    </div>
    <div class="info-panel">
      <p class="info-panel__tagline">Visual Effects Studio</p>
      <span class="info-panel__rule"></span>
      <ul class="contact">
        <li><span class="contact__label">m:</span> +1 555 014 2290</li>
        <li><span class="contact__label">e:</span> hello@embervale.example</li>
      </ul>
    </div>
  </section>

  <section class="card card--back">
    <div class="brand">
      <span class="brand__dot"></span>
      <span class="brand__name">The Ember Vale</span>
    </div>
    <div class="debris-art" role="img" aria-label="Rendered shards of shattered metal flying up from the ground"></div>
    <p class="web">www.embervale.example</p>
  </section>
</body>
</html>
```